New Phone Case requires logo and packaging

We need a nice and sleek logo designed along with packaging for our Premium Phone Case brand

Our Brand Name is Vaxel
Please note this has nothing to do with a Rhino so don't put a Rhino in the logo
I've also attached a file called VAXEL Logo Inspiration, which shows something along the lines of the type of text we want to use. Please note i have photoshopped that image together from another logo we had, and i liked the text, but its for you to see what direction we want to go in. Also note i have shown different variations in that image file, use your imagination with it and show us a nice and clean logo.

We would like the Brand in upper caps such as VAXEL
The brand is for Premium Phone Cases. The first thing that should come to someones mind when looking at the branding is High Quality, Premium and Modern.

The look must be high end and modern

The design must portray high quality and premium!

Also i will say "Less is More". Don't cramp many things on the packaging and logo. We just want a nice, clean cut high quality logo and packaging

I have attached images of an example packaging from a few competitors. One is a standard open from top packaging, while another is a slide out packaging. Our packaging dimensions should be the same which are Packaging dimensions
Length = 18cm
Height = 1.5cm
Depth = 9.5cm

Also note the example packaging has a transparent front section to show which case is inside, this is optional if you want to have it. If not you can cover it all up.

Font styles to use
Other font styles liked:
• Any nice font but just not the standard everyday stuff like Arial, San Serif etc as i want it to be differentiated. A Font that shows Serious Quality and one that stands out would be awesome!

Colors

Designer to choose colors to be used in the design.

Requirements
Must have
• Must be a nice and clean design
• Packaging dimensions
• Length = 18cm
• Height = 1.5cm
• Depth = 9.5cm

```html
<!DOCTYPE html>
<html lang="en">
<head>
<meta charset="utf-8">
<title>Vaxel — Packaging Artwork</title>
<link href="https://fonts.googleapis.com/css2?family=Bodoni+Moda:wght@400;500&family=Poppins:wght@300&display=swap" rel="stylesheet">
<style>
  :root {
    --page-bg: #f4f4f4;
    --panel-black: #141414;
    --gold: #d9a440;
    --gold-soft: #b8893a;
  }
  html, body {
    margin: 0;
    padding: 0;
    width: 1200px;
    height: 1200px;
    overflow: hidden;
    background: var(--page-bg);
  }
  .canvas {
    position: relative;
    width: 1200px;
    height: 1200px;
  }
  .pack-panel {
    position: absolute;
    left: 0;
    top: 270px;
    width: 1200px;
    height: 660px;
    background: var(--panel-black);
    color: var(--gold);
  }
  .brand-wordmark {
    position: absolute;
    left: 155px;
    top: 138px;
    margin: 0;
    font-family: "Bodoni Moda", serif;
    font-weight: 500;
    font-size: 92px;
    line-height: 1;
    letter-spacing: 0.2em;
    color: var(--gold);
  }
  .brand-rule {
    position: absolute;
    left: 135px;
    top: 497px;
    width: 357px;
    height: 40px;
  }
  .brand-rule-name {
    position: absolute;
    left: 0;
    right: 0;
    top: 8px;
    text-align: center;
    font-family: "Bodoni Moda", serif;
    font-weight: 500;
    font-size: 20px;
    letter-spacing: 0.12em;
    color: var(--gold);
  }
  .brand-rule svg {
    position: absolute;
    left: 0;
    top: 0;
  }
  .features {
    position: absolute;
    left: 690px;
    top: 432px;
    width: 450px;
    text-align: center;
  }
  .features-title {
    margin: 0;
    font-family: "Bodoni Moda", serif;
    font-weight: 400;
    font-size: 33px;
    line-height: 1;
    letter-spacing: 0.3em;
    color: var(--gold);
    white-space: nowrap;
  }
  .features-label {
    margin: 20px 0 0;
    font-family: "Poppins", sans-serif;
    font-weight: 300;
    font-size: 11px;
    color: var(--gold);
  }
  .features-divider {
    width: 292px;
    height: 1px;
    margin: 5px auto 6px;
    background: var(--gold-soft);
  }
  .features-list {
    list-style: none;
    margin: 0;
    padding: 0;
    font-family: "Poppins", sans-serif;
    font-weight: 300;
    font-size: 11px;
    line-height: 13px;
    color: var(--gold);
  }
</style>
</head>
<body>
<main class="canvas">
  <section class="pack-panel">
    <h1 class="brand-wordmark">VAXEL</h1>

    <div class="brand-rule">
      <svg width="357" height="40" viewBox="0 0 357 40" aria-hidden="true">
        <line x1="0" y1="20" x2="142" y2="20" stroke="#b8893a" stroke-width="1.5"/>
        <line x1="215" y1="20" x2="357" y2="20" stroke="#b8893a" stroke-width="1.5"/>
      </svg>
      <span class="brand-rule-name">VAXEL</span>
    </div>

    <div class="features">
      <h2 class="features-title">BEST PROTECTION</h2>
      <p class="features-label">key features</p>
      <div class="features-divider"></div>
      <ul class="features-list">
        <li>offers complete front and backside protection</li>
        <li>perfectly slim fit with phone</li>
        <li>rubberized coating offers superior grip and comfortable feel</li>
      </ul>
    </div>
  </section>
</main>
</body>
</html>
```